Wedding Invitation and envelope package

I need the 1st of many invitation designs. This is a floral collection and I have attached many designs that I like from competitors. I think that the pastel look is the best but I am hoping you can make something special. The font selection is just as important as the imagery. The overall size with bleeds is 5.25 x 7.25" and I have attached a sample to make sure sizing is clear. I also need A7 envelopes to go with the invitation, front and back flap. I want someone to look at the design and say they would pick it over any of the samples. I will need 8 total floral designs done over the next few weeks after this 1st one is done. I will also need a collection of 8 modern designs done. Please ask any questions

Font styles to use
Serif
Sans Serif
Script

Requirements
Must have
• This is a single sided invitation, a back side is not needed.
Should not have
• No full solid dark backgrounds

```html
<!DOCTYPE html>
<html lang="en">
<head>
<meta charset="utf-8">
<title>Wedding Invitation Suite – Clara &amp; Daniel</title>
<link href="https://fonts.googleapis.com/css2?family=Montserrat:wght@400;500;600;700&family=Playfair+Display:wght@400;700&family=Kaushan+Script&display=swap" rel="stylesheet">
<style>
  :root{
    --page:#ececea;
    --paper:#ffffff;
    --ink:#3b3b3d;
    --ink-soft:#6a6a6c;
    --script:#1f1f21;
    --peach:#f7cdbd;
    --peach-light:#fbe4da;
    --blush:#f1b8b0;
    --rose:#e9a19b;
    --leaf:#b9cdb4;
    --gold:#d8b16c;
    --line:#c9c9c9;
  }
  *{margin:0;padding:0;box-sizing:border-box}
  html,body{width:1200px;height:2400px;overflow:hidden}
  body{background:var(--page);position:relative;font-family:"Montserrat",sans-serif;color:var(--ink)}

  .invitation{position:absolute;left:50px;top:110px;width:1100px;height:1519px;background:var(--paper);box-shadow:0 6px 24px rgba(0,0,0,.12);overflow:hidden}
  .invitation > *{position:absolute}
  .wash{left:0;top:0;width:100%;height:100%}

  .floral{border-radius:48% 52% 46% 54% / 55% 45% 55% 45%}
  .floral-top{left:-20px;top:-20px;width:330px;height:300px;background:linear-gradient(150deg,var(--blush) 0%,var(--peach) 45%,var(--leaf) 100%);opacity:.85}
  .floral-side{left:800px;top:720px;width:320px;height:480px;background:linear-gradient(200deg,var(--leaf) 0%,var(--blush) 45%,var(--peach) 75%,var(--leaf) 100%);opacity:.85}

  .intro{left:257px;top:58px;width:460px;font-size:24px;font-weight:600;line-height:1.35;color:var(--ink);text-transform:capitalize}
  .frame{left:183px;top:348px;width:734px;height:734px}

  .couple{left:150px;width:780px;text-align:center;color:var(--ink)}
  .first-name{font-size:96px;font-weight:400;letter-spacing:6px;line-height:1}
  .surname{font-size:30px;font-weight:400;letter-spacing:13px;line-height:1}
  .name-1{top:380px}
  .surname-1{top:494px}
  .ampersand{left:150px;top:540px;width:780px;text-align:center;font-family:"Playfair Display",serif;font-weight:700;font-size:120px;line-height:1}
  .name-2{top:690px}
  .surname-2{top:804px}

  .date-row{left:165px;top:900px;width:620px;height:170px}
  .date-row > *{position:absolute}
  .rule{height:2px;background:var(--ink)}
  .rule-day-top{left:0;top:28px;width:230px}
  .rule-day-bottom{left:0;top:140px;width:230px}
  .rule-time-top{left:400px;top:28px;width:210px}
  .rule-time-bottom{left:400px;top:140px;width:210px}
  .divider{width:2px;top:15px;height:140px;background:var(--ink)}
  .divider-1{left:250px}
  .divider-2{left:380px}
  .day,.time{top:62px;font-size:38px;font-weight:600;letter-spacing:2px}
  .day{left:0;width:230px}
  .time{left:400px;width:210px;text-align:center}
  .date{left:255px;width:120px;text-align:center;top:8px}
  .date .month,.date .year{display:block;font-size:28px;font-weight:500;letter-spacing:2px;line-height:1.2}
  .date .dd{display:block;font-size:72px;font-weight:700;line-height:1}
  .venue{left:165px;top:1110px;font-size:26px;font-weight:500;color:var(--ink)}

  .envelope{position:absolute;top:1770px;width:540px;height:391px;background:var(--paper);box-shadow:0 6px 20px rgba(0,0,0,.12);overflow:hidden}
  .envelope > *{position:absolute}
  .envelope-front{left:40px}
  .envelope-back{left:620px}
  .env-floral-top{left:-10px;top:-10px;width:130px;height:110px;border-radius:46% 54% 52% 48% / 50% 50% 50% 50%;background:linear-gradient(150deg,var(--blush),var(--peach) 50%,var(--leaf));opacity:.85}
  .env-floral-bottom{right:-10px;bottom:-10px;width:120px;height:110px;border-radius:52% 48% 46% 54% / 50% 50% 50% 50%;background:linear-gradient(330deg,var(--blush),var(--peach) 50%,var(--leaf));opacity:.85}
  .guest{left:0;top:130px;width:100%;text-align:center;font-family:"Kaushan Script",cursive;font-size:54px;line-height:1.2;color:var(--script)}
  .addr{left:0;width:100%;text-align:center;font-size:17px;font-weight:500;color:var(--ink-soft)}
  .guest-addr{top:218px}
  .accent-line{left:240px;width:60px;height:3px;background:var(--blush)}
  .guest-line{top:250px}
  .flap{left:0;top:0;width:540px;height:391px}
  .return{left:0;top:26px;width:100%;text-align:center;font-family:"Kaushan Script",cursive;font-size:36px;line-height:1.2;color:var(--script)}
  .return-addr{top:84px}
  .return-line{top:114px}
</style>
</head>
<body>

<section class="invitation" aria-label="Wedding invitation">
  <svg class="wash" viewBox="0 0 1100 1519" aria-hidden="true">
    <defs>
      <radialGradient id="washTop" cx="0.5" cy="0.5" r="0.5">
        <stop offset="0" stop-color="#f7cdbd" stop-opacity=".95"/>
        <stop offset=".7" stop-color="#fbe4da" stop-opacity=".6"/>
        <stop offset="1" stop-color="#fbe4da" stop-opacity="0"/>
      </radialGradient>
      <radialGradient id="washBottom" cx="0.5" cy="0.5" r="0.5">
        <stop offset="0" stop-color="#f7cdbd" stop-opacity=".8"/>
        <stop offset="1" stop-color="#fbe4da" stop-opacity="0"/>
      </radialGradient>
    </defs>
    <ellipse cx="560" cy="420" rx="620" ry="420" fill="url(#washTop)"/>
    <ellipse cx="250" cy="1300" rx="420" ry="260" fill="url(#washBottom)"/>
  </svg>

  <div class="floral floral-top" role="img" aria-label="Watercolour cluster of blush roses and sage leaves"></div>
  <div class="floral floral-side" role="img" aria-label="Watercolour spray of blush roses, buds and eucalyptus leaves"></div>

  <p class="intro">Together with our families we cordially invite you on their wedding day</p>

  <svg class="frame" viewBox="0 0 734 734" aria-hidden="true">
    <circle cx="367" cy="367" r="360" fill="none" stroke="var(--gold)" stroke-width="5"/>
    <circle cx="372" cy="362" r="352" fill="none" stroke="var(--gold)" stroke-width="2" opacity=".6"/>
  </svg>

  <h1 class="couple first-name name-1">CLARA</h1>
  <p class="couple surname surname-1">WHITFIELD</p>
  <p class="ampersand">&amp;</p>
  <h1 class="couple first-name name-2">DANIEL</h1>
  <p class="couple surname surname-2">MARSH</p>

  <div class="date-row">
    <span class="rule rule-day-top"></span>
    <span class="rule rule-day-bottom"></span>
    <span class="day">SATURDAY</span>
    <span class="divider divider-1"></span>
    <span class="date"><span class="month">APR</span><span class="dd">25</span><span class="year">2020</span></span>
    <span class="divider divider-2"></span>
    <span class="rule rule-time-top"></span>
    <span class="rule rule-time-bottom"></span>
    <span class="time">2:00 PM</span>
  </div>

  <p class="venue">Street Address City, State Zip</p>
</section>

<section class="envelope envelope-front" aria-label="Envelope front">
  <div class="env-floral-top" role="img" aria-label="Small watercolour rose cluster"></div>
  <p class="guest">Mr. and Mrs.Guest</p>
  <p class="addr guest-addr">Street Address City, State Zip</p>
  <span class="accent-line guest-line"></span>
  <div class="env-floral-bottom" role="img" aria-label="Small watercolour rose cluster"></div>
</section>

<section class="envelope envelope-back" aria-label="Envelope back flap">
  <svg class="flap" viewBox="0 0 540 391" aria-hidden="true">
    <path d="M0 0 L270 150 L540 0" fill="none" stroke="var(--line)" stroke-width="2"/>
  </svg>
  <p class="return">Return Address</p>
  <p class="addr return-addr">Street Address City, State Zip</p>
  <span class="accent-line return-line"></span>
</section>

</body>
</html>
```